zorvantix Web Design Project

It is a virtual assistance/concierge company that helps the busy professional by remotely providing administrative, technical and/or creative business support services, specializing in the medical device industry. Company name is zorvantix.
(website will be zorvantix.com)

Allowing things to be done without taking time away from more urgent issues or family/personal time. Partnering with a VA reduces stress, protects cash flow, eliminates administrative hassles, and enables business people to find the success they originally set out to achieve. Saves small businesses and/or individuals on overhead, salary, et. Work is done remotely to offer administrative, clerical, typing and specialist service assistance on a regular, ad-hoc or emergency cover basis.

Though we are capable of addressing the needs of medical professionals and industry representatives due to our experience and knowledge (sales, HCC guidelines, etc.) we do not want to be limited to that market only.

Target Market(s)

Target market would be M/F, 30-50, National, busy, Alpha, entrepreneurs and industry professionals who want/need to do more without sacrifice of life

Industry/Entity Type

Industry

Requirements
Nice to have
• We do have a logo designed via the MarqueLoom website that can/should be included. Logo is uploaded.

```html
<!DOCTYPE html>
<html lang="en">
<head>
<meta charset="utf-8">
<title>zorvantix.com — Home</title>
<link rel="stylesheet" href="https://fonts.googleapis.com/css2?family=Arimo:wght@400;700&family=PT+Sans:wght@400;700&display=swap">
<style>
:root{
  --blue:#0a5aa5;
  --blue-dark:#0a3f7c;
  --blue-deep:#083468;
  --blue-light:#4aa3e8;
  --orange:#f7a21b;
  --orange-dark:#e07a05;
  --red:#c8102e;
  --ink:#333;
  --muted:#666;
  --line:#dcdcdc;
  --panel:#f3f3f3;
  --charcoal:#2e2e2e;
  --white:#fff;
}
*{box-sizing:border-box;margin:0;padding:0}
html,body{width:972px;height:1200px;overflow:hidden}
body{position:relative;font-family:"Arimo",Arial,sans-serif;color:var(--ink);
  background:linear-gradient(#fafafa 0,#e9e9e9 300px,#fff 310px,#fff 924px)}
.abs{position:absolute}
h1,h2,h3,.head{font-family:"PT Sans",Arial,sans-serif;font-weight:400}

/* header */
.brand{left:156px;top:22px;display:flex;align-items:center;gap:8px}
.brand-dot{width:22px;height:22px;border-radius:50%;background:var(--blue-dark)}
.brand-name{font-family:"PT Sans",Arial,sans-serif;font-weight:700;font-size:34px;color:var(--red);letter-spacing:-.5px;line-height:1}
.callus{right:175px;top:11px;font-family:"PT Sans",Arial,sans-serif;font-weight:700;color:#555;font-size:15px}
.callus strong{font-size:22px;color:#444;margin-left:4px}
.mainnav{left:339px;top:41px;width:477px;height:26px;border-radius:13px;
  background:linear-gradient(var(--blue-light),var(--blue) 55%,var(--blue-dark));display:flex;align-items:center;padding-left:8px;
  box-shadow:0 2px 3px rgba(0,0,0,.25)}
.mainnav a{color:var(--white);text-decoration:none;font-size:9px;font-weight:700;padding:0 10px;height:26px;line-height:26px;text-transform:uppercase}
.mainnav a.active{background:linear-gradient(#888,#555);border-radius:13px 0 0 13px;margin-left:-8px;padding:0 14px}
.mainnav .caret::after{content:" ▾";font-size:8px}

/* hero */
.hero{left:156px;top:78px;width:660px;height:211px;box-shadow:0 6px 8px rgba(0,0,0,.25)}
.hero-bar{height:26px;background:linear-gradient(#6a6a6a,#4a4a4a);display:flex;justify-content:flex-end;align-items:center;gap:6px;padding-right:12px}
.hero-bar span{background:#3a3a3a;border:1px solid #777;border-radius:3px;color:#ddd;font-size:8.5px;padding:3px 9px}
.hero-stage{position:relative;height:185px;background:linear-gradient(160deg,#1b78c8,#0b4e95 60%,#0a3f7c)}
.hero-title{position:absolute;left:59px;top:38px;color:var(--white);font-size:25px}
.hero-sub{position:absolute;left:59px;top:74px;color:var(--white);font-size:13px;font-weight:700}
.btn-orange{background:linear-gradient(#ffc13d,var(--orange) 50%,var(--orange-dark));color:#6a2e00;font-family:"PT Sans",Arial,sans-serif;font-weight:700;border-radius:6px;display:flex;align-items:center;justify-content:center;gap:10px;box-shadow:0 3px 5px rgba(0,0,0,.3)}
.btn-orange i{width:16px;height:16px;border:2px solid #6a2e00;border-radius:50%;position:relative}
.btn-orange i::after{content:"";position:absolute;left:4px;top:2.5px;border-left:6px solid #6a2e00;border-top:3.5px solid transparent;border-bottom:3.5px solid transparent}
.hero-cta{position:absolute;left:60px;top:105px;width:142px;height:34px;font-size:15px}
.hero-photo{position:absolute;right:0;top:0;width:297px;height:185px;background:linear-gradient(120deg,#2b6fae,#1a3550 55%,#d7c2a8)}
.hero-dots{position:absolute;left:280px;bottom:0;width:100px;height:16px;background:linear-gradient(#eee,#bbb);border-radius:8px 8px 0 0;display:flex;gap:5px;justify-content:center;align-items:center}
.hero-dots b{width:8px;height:8px;border-radius:50%;background:#555}
.hero-dots b.on{background:var(--blue)}

/* left column */
.intro{left:156px;top:326px;width:376px}
.section-title{color:var(--blue);font-size:19px}
.intro-body{margin-top:8px;font-size:9.6px;line-height:15.2px;color:#444}
.intro-mark{float:left;width:54px;height:60px;margin:2px 12px 0 4px;display:flex;align-items:flex-start;justify-content:center}
.intro-mark span{width:30px;height:30px;border-radius:50%;background:var(--red)}
.intro-body p{text-align:justify}
.intro-body p+p{margin-top:2px}
.rule{left:156px;width:376px;height:1px;background:var(--line)}
.services{left:156px;top:526px;width:376px}
.service-grid{display:grid;grid-template-columns:194px 182px;row-gap:22px;margin-top:6px}
.service{display:flex;gap:10px}
.service .icon{width:40px;height:40px;border-radius:6px;flex:none}
.service h3{color:var(--blue);font-size:13.5px;margin-bottom:3px}
.service p{font-size:9.6px;line-height:15px;color:#444}
.newsletter{left:156px;top:730px;width:377px;height:61px;border-radius:4px;
  background:linear-gradient(#ffc53f,var(--orange) 55%,var(--orange-dark));box-shadow:0 2px 4px rgba(0,0,0,.3)}
.news-art{position:absolute;left:10px;top:-5px;width:68px;height:62px;border-radius:4px;background:linear-gradient(135deg,#d8ecfb,#7fb5e2)}
.news-title{position:absolute;left:100px;top:5px;color:#5a2a00;font-family:"PT Sans",Arial,sans-serif;font-size:15px}
.news-sub{position:absolute;left:100px;top:22px;color:#7a3a00;font-size:9px;font-style:italic}
.news-input{position:absolute;left:101px;top:36px;width:115px;height:15px;background:var(--white);border:1px solid #d48a1a;font-size:8.5px;color:#aaa;font-style:italic;padding:2px 5px}
.news-btn{position:absolute;left:221px;top:36px;width:66px;height:15px;background:#3b3b3b;border-radius:2px;color:var(--white);font-size:9.5px;font-weight:700;display:flex;align-items:center;justify-content:center;gap:10px}
.news-btn i{width:9px;height:9px;border:1.5px solid #fff;border-radius:50%}

/* right column */
.video{left:557px;top:323px;width:259px;height:164px;background:#222}
.video-frame{position:absolute;left:0;top:16px;width:259px;height:132px;background:linear-gradient(100deg,#cfe1f0,#8fb1cc 45%,#c59a7d)}
.video-play{position:absolute;left:99px;top:50px;width:60px;height:44px;border-radius:8px;background:rgba(255,255,255,.85)}
.video-play::after{content:"";position:absolute;left:23px;top:12px;border-left:18px solid #222;border-top:10px solid transparent;border-bottom:10px solid transparent}
.video-bar{position:absolute;left:0;bottom:0;width:259px;height:16px;background:linear-gradient(#eee,#bbb);font-size:7.5px;color:#333;display:flex;align-items:center;gap:8px;padding:0 6px}
.video-track{width:60px;height:4px;border-radius:2px;background:#888}
.form-box{left:557px;top:504px;width:259px;height:253px;background:var(--panel);border:1px solid var(--line)}
.form-head{height:47px;background:linear-gradient(#1a75c4,var(--blue-dark));color:var(--white);font-family:"PT Sans",Arial,sans-serif;font-size:14px;line-height:17px;padding:6px 0 0 18px}
.form-row{position:absolute;left:19px;display:flex;align-items:center}
.form-row label{width:90px;font-size:8.5px;font-weight:700;color:#444}
.form-row span{display:block;width:130px;height:16px;background:var(--white);border:1px solid #ccc}
.form-row span.short{width:109px}
.form-row em{width:15px;height:15px;border-radius:50%;background:#ccc;margin-left:5px}
.form-submit{position:absolute;left:110px;top:163px;width:129px;height:33px;font-size:14px}
.privacy{position:absolute;left:20px;top:210px;display:flex;gap:12px}
.lock{width:31px;height:30px;border-radius:4px;background:linear-gradient(#fff,#ddd);border:1px solid #ccc;display:flex;align-items:center;justify-content:center}
.privacy p{width:184px;font-size:7px;line-height:9px;color:#555}
.testimonial{left:557px;top:773px;width:259px;height:116px;background:var(--panel);border:1px solid var(--line)}
.testi-photo{position:absolute;left:14px;top:14px;width:67px;height:86px;background:linear-gradient(#b7cbd9,#8a9aa5);border:4px solid var(--white);box-shadow:0 1px 3px rgba(0,0,0,.35);transform:rotate(-3deg)}
.testi-title{position:absolute;left:97px;top:8px;color:var(--blue);font-size:17px}
.testi-text{position:absolute;left:97px;top:31px;width:150px;font-size:9.5px;line-height:12.5px;color:#555}
.testi-name{position:absolute;left:97px;top:80px;font-size:9px;font-weight:700;color:#333}
.testi-place{position:absolute;left:97px;top:92px;font-size:8px;color:#aaa}
.testi-quote{position:absolute;right:18px;top:72px;font-family:"PT Sans",Arial,sans-serif;font-size:42px;color:#bbb;font-weight:700}

/* partner strip */
.partners{left:0;top:924px;width:972px;height:41px;background:linear-gradient(#fff,#e4e4e4);border-top:1px solid var(--line)}
.partner-arrow{position:absolute;top:13px;width:15px;height:15px;border-radius:50%;background:#bbb}
.partner-row{position:absolute;left:234px;top:11px;width:500px;display:flex;justify-content:space-between;align-items:center}
.partner-row i{height:18px;border-radius:3px;background:#c9c9c9}

/* footer */
.footer{left:0;top:965px;width:972px;height:193px;background:linear-gradient(var(--blue-deep),#0b4a8d 60%,#0a3f7c)}
.foot-title{position:absolute;top:26px;color:var(--blue-light);font-size:19px}
.foot-about{position:absolute;left:157px;top:57px;width:362px;color:var(--white);font-size:12.5px;line-height:18.5px}
.foot-about .hl{color:var(--blue-light)}
.foot-about .q{font-family:"PT Sans",Arial,sans-serif;font-weight:700;font-size:24px;line-height:0;vertical-align:-6px}
.foot-map{position:absolute;left:722px;top:40px;width:90px;height:110px;border-radius:10px;background:radial-gradient(circle at 50% 50%,#6ab1ec,#2e7fc5)}
.foot-address{position:absolute;z-index:1;left:572px;top:60px;color:var(--white);font-size:9.5px;line-height:17px;white-space:nowrap}
.foot-address strong{font-size:12px}
.foot-phone{position:absolute;z-index:1;left:572px;top:120px;width:138px;height:24px;border-radius:12px;background:linear-gradient(#ffc13d,var(--orange-dark));color:#6a2e00;font-family:"PT Sans",Arial,sans-serif;font-weight:700;font-size:14px;display:flex;align-items:center;gap:7px;padding-left:6px}
.bottom{left:0;top:1158px;width:972px;height:42px;background:linear-gradient(#3a3a3a,var(--charcoal))}
.bottom-links{position:absolute;left:157px;top:17px;font-size:8.5px;color:#aaa}
.bottom-brand{position:absolute;left:548px;top:9px;font-family:"PT Sans",Arial,sans-serif;font-weight:700;font-size:22px;color:#777;display:flex;align-items:center;gap:6px}
.bottom-brand i{width:10px;height:10px;border-radius:50%;background:#777}
.social{position:absolute;left:676px;top:15px;display:flex;align-items:center;gap:4px}
.social span{background:#555;color:#ddd;font-size:7.5px;padding:2px 5px;border-radius:2px;margin-right:2px}
.social i{width:11px;height:11px;border-radius:2px;background:#8a8a8a}
</style>
</head>
<body>

<header>
  <div class="abs brand"><span class="brand-dot"></span><span class="brand-name">zorvantix</span></div>
  <div class="abs callus">CALL US <strong>555-013-7746</strong></div>
  <nav class="abs mainnav">
    <a class="active" href="#">Home</a>
    <a class="caret" href="#">About</a>
    <a class="caret" href="#">Solutions</a>
    <a href="#">Products</a>
    <a class="caret" href="#">Services</a>
    <a href="#">Consulting</a>
    <a class="caret" href="#">Resources</a>
  </nav>
</header>

<section class="abs hero">
  <div class="hero-bar"><span>✉ Contact</span><span>💬 Chat With Sales</span><span>👤 Client Portal</span></div>
  <div class="hero-stage">
    <h1 class="hero-title">The zorvantix.com</h1>
    <p class="hero-sub">Lorum ipsum dolor sit amet businesses</p>
    <a class="btn-orange hero-cta">Find Out More <i></i></a>
    <div class="hero-photo" role="img" aria-label="Two business professionals smiling at a laptop"></div>
    <div class="hero-dots"><b></b><b class="on"></b><b></b><b></b><b></b></div>
  </div>
</section>

<section class="abs intro">
  <h2 class="section-title">The zorvantix.com</h2>
  <div class="intro-body">
    <div class="intro-mark"><span></span></div>
    <p><strong>Today's small and medium sized businesses</strong> are faced with a major challenge. Your business depends upon technology to operate, move forward, and grow. However, technology is constantly changing and you don't have an unlimited pool of resources.</p>
    <p>At Quillmarsh Technology Solutions, we partner with you to serve as your technology consultant and can provide a custom IT solution for your business that gives you modern technology, unlimited support, cost certainty, and most importantly, peace of mind.</p>
  </div>
</section>

<div class="abs rule" style="top:509px"></div>

<section class="abs services">
  <h2 class="section-title">Our Services</h2>
  <div class="service-grid">
    <div class="service"><div class="icon" role="img" aria-label="Satellite antenna illustration" style="background:linear-gradient(#e8eef4,#9fb3c6)"></div><div><h3>Infrastructure Solutions</h3><p>Lorem ipsum dolor sit amet,<br>conseter adipiscing elit.</p></div></div>
    <div class="service"><div class="icon" role="img" aria-label="Support person silhouette illustration" style="background:linear-gradient(#f4f4f4,#bdbdbd)"></div><div><h3>IT Support</h3><p>Lorem ipsum dolor sit amet,<br>conseter adipiscing elit.</p></div></div>
    <div class="service"><div class="icon" role="img" aria-label="Globe with cursor illustration" style="background:linear-gradient(#bfe0a8,#3f7fbf)"></div><div><h3>Cloud Solutions</h3><p>Lorem ipsum dolor sit amet,<br>conseter adipiscing elit.</p></div></div>
    <div class="service"><div class="icon" role="img" aria-label="Networked computers illustration" style="background:linear-gradient(#dbe8f4,#6f97bd)"></div><div><h3>VoIP Services</h3><p>Lorem ipsum dolor sit amet,<br>conseter adipiscing elit.</p></div></div>
  </div>
</section>

<div class="abs rule" style="top:709px"></div>

<section class="abs newsletter">
  <div class="news-art" role="img" aria-label="Stack of envelopes illustration"></div>
  <p class="news-title">SignUp for Our Newsletter</p>
  <p class="news-sub">and start receiving our new-look weekly email Newsletter</p>
  <div class="news-input">Enter your email address</div>
  <div class="news-btn">Submit <i></i></div>
</section>

<section class="abs video">
  <div class="video-frame" role="img" aria-label="Video still of a support agent wearing a headset"></div>
  <div class="video-play"></div>
  <div class="video-bar"><span>❚❚</span><span>◀)</span><span>0:00 / 0:00</span><span class="video-track"></span><span style="margin-left:auto">360p ▲</span><span>⤢</span></div>
</section>

<section class="abs form-box">
  <h2 class="form-head">16 Critical Questions You Must Ask<br>Before Hiring Any IT Company</h2>
  <div class="form-row" style="top:59px"><label>Company Name</label><span></span></div>
  <div class="form-row" style="top:80px"><label>First Name</label><span></span></div>
  <div class="form-row" style="top:101px"><label>Last Name</label><span></span></div>
  <div class="form-row" style="top:121px"><label>Email Address</label><span class="short"></span><em></em></div>
  <div class="form-row" style="top:142px"><label>Phone Number</label><span></span></div>
  <a class="btn-orange form-submit">Submit Form <i></i></a>
  <div class="privacy">
    <div class="lock"><svg width="14" height="17" viewBox="0 0 14 17"><path d="M3 7V5a4 4 0 0 1 8 0v2" fill="none" stroke="#b07a10" stroke-width="2"/><rect x="1" y="7" width="12" height="9" rx="1.5" fill="#e0a21b"/></svg></div>
    <p>* We respect your privacy. Your information will never be given to another party, and you can opt out from our communications anytime you wish.</p>
  </div>
</section>

<section class="abs testimonial">
  <div class="testi-photo" role="img" aria-label="Portrait photo of a smiling client"></div>
  <h2 class="testi-title">Testimonial</h2>
  <p class="testi-text">Donec eget tellus non erat lacinia Donec in velit vel ipsum auctor pul Proin ullamcorper urna.</p>
  <p class="testi-name">Dale Ormond</p>
  <p class="testi-place">Santa Monica, USA</p>
  <span class="testi-quote">”</span>
</section>

<section class="abs partners" aria-label="Technology partners">
  <span class="partner-arrow" style="left:158px"></span>
  <div class="partner-row">
    <i style="width:56px"></i><i style="width:24px;border-radius:50%;height:24px"></i><i style="width:46px"></i><i style="width:58px"></i><i style="width:48px"></i><i style="width:50px"></i><i style="width:76px"></i>
  </div>
  <span class="partner-arrow" style="left:798px"></span>
</section>

<footer class="abs footer">
  <h2 class="foot-title" style="left:157px">Who We Are?</h2>
  <p class="foot-about"><span class="q hl">“</span> <span class="hl">zorvantix.com Solutions</span> is a total IT solutions partner for small and medium sized businesses in the Dallas / Fort Worth metroplex. Our services are meant to ensure that technology has a positive affect for your business, your employee's productivity, and your bottom line. <span class="q">”</span></p>
  <h2 class="foot-title" style="left:572px">Address</h2>
  <div class="foot-map" role="img" aria-label="Map of Texas with office location marker"></div>
  <p class="foot-address"><strong>4470 Elmcrest Parkway</strong><br>Suite 208-61<br>Lakemont, Texas 75099</p>
  <div class="foot-phone"><svg width="22" height="16" viewBox="0 0 22 16"><rect x="1" y="5" width="20" height="10" rx="2" fill="#fff"/><path d="M2 6C4 1 18 1 20 6" fill="none" stroke="#fff" stroke-width="3"/><circle cx="11" cy="10" r="2.5" fill="#888"/></svg>555-013-7746</div>
</footer>

<div class="abs bottom">
  <p class="bottom-links">© 2011 zorvantix.com &nbsp;|&nbsp; Terms of Use &nbsp;|&nbsp; Privacy Policy &nbsp;|&nbsp; Site Map</p>
  <div class="bottom-brand"><i></i>zorvantix</div>
  <div class="social"><span>Social Media</span><i></i><i></i><i></i><i></i><i></i></div>
</div>

</body>
</html>
```